Business card design needed for a security services business.

We provide a wide range of security services from guard personnel to electronic systems.

Industry/Entity Type

Security Industry

Contact Information for Business Card

Brent Holloway, Owner Office: 780.555.0148; Cell: 780.555.0193 Email: brent@korvanshieldgroup.example; Address 20417 163 St Edmonton, AB T5X 2K8

Colors
0054AA
0677BA
7BADD7
CADEEF
E8F1F8

Requirements
Nice to have
• On the back of the card I would like to possible list the services I provide: Guards Mobiles Live Video Surveillance Access Intrusion

```html
<!DOCTYPE html>
<html lang="en">
<head>
<meta charset="utf-8">
<title>Korvan Shield Group – Business Card</title>
<link rel="stylesheet" href="https://fonts.googleapis.com/css2?family=Open+Sans:wght@400;600;700&display=swap">
<style>
  :root {
    --backdrop: #3b3b3c;
    --card: #131314;
    --edge-blue: #0677BA;
    --brand-blue: #0677BA;
    --text-light: #f2f2f2;
    --emboss: #2a2a2c;
    --emboss-line: #6a6a6e;
  }
  * { box-sizing: border-box; margin: 0; padding: 0; }
  html, body {
    width: 1200px; height: 801px; overflow: hidden;
    background: var(--backdrop);
    font-family: "Open Sans", Arial, sans-serif;
  }
  .stage {
    width: 1200px; height: 801px;
    display: flex; align-items: center; justify-content: center; gap: 40px;
  }
  .card {
    position: relative;
    width: 540px; height: 309px;
    background: var(--card);
    border-bottom: 3px solid var(--edge-blue);
    border-right: 3px solid var(--edge-blue);
    box-shadow: 0 14px 30px rgba(0,0,0,.45);
    color: var(--text-light);
    white-space: nowrap;
  }

  /* Front */
  .brand {
    position: absolute; left: 34px; top: 62px;
    display: flex; align-items: center; gap: 9px;
  }
  .brand-square { width: 15px; height: 15px; background: var(--brand-blue); flex: none; }
  .brand-name {
    font-weight: 700; font-size: 16px; letter-spacing: .6px;
    color: var(--brand-blue); text-transform: uppercase;
  }
  .brand-rule {
    position: absolute; left: 58px; top: 96px; width: 196px;
    height: 1px; background: var(--text-light);
  }
  .person {
    position: absolute; right: 34px; top: 30px; text-align: right;
  }
  .person-name {
    font-weight: 700; font-size: 17px; letter-spacing: .5px;
    color: var(--brand-blue); text-transform: uppercase;
  }
  .person-title { font-size: 12px; color: var(--text-light); margin-top: 2px; }
  .divider {
    position: absolute; left: 34px; right: 34px; top: 128px;
    height: 1px; background: var(--edge-blue);
  }
  .address {
    position: absolute; right: 34px; top: 140px; text-align: right;
    font-size: 12px; line-height: 1.5; color: var(--text-light);
  }
  .contacts {
    position: absolute; left: 34px; bottom: 28px;
    list-style: none; font-size: 13px; line-height: 1.6;
  }
  .contacts li { display: flex; align-items: center; gap: 9px; }
  .contacts svg { width: 11px; height: 11px; fill: var(--edge-blue); flex: none; }

  /* Back */
  .emboss-brand {
    position: absolute; left: 0; right: 0; top: 92px; text-align: center;
  }
  .emboss-name {
    font-weight: 700; font-size: 32px; letter-spacing: 3px;
    color: var(--emboss); text-transform: uppercase;
    text-shadow: 0 1px 0 #3d3d40;
  }
  .emboss-rule {
    width: 330px; height: 1px; margin: 12px auto 0;
    background: linear-gradient(90deg, transparent, var(--emboss-line), transparent);
  }
  .services {
    position: absolute; left: 0; right: 0; bottom: 40px; text-align: center;
    font-size: 13px; letter-spacing: .8px; text-transform: uppercase;
    color: var(--text-light);
  }
</style>
</head>
<body>
<main class="stage">
  <section class="card card-front" aria-label="Card front">
    <div class="brand">
      <span class="brand-square"></span>
      <span class="brand-name">Korvan Shield Group</span>
    </div>
    <div class="brand-rule"></div>
    <div class="person">
      <p class="person-name">Brent Holloway</p>
      <p class="person-title">Owner</p>
    </div>
    <div class="divider"></div>
    <p class="address">20417 163 St Edmonton<br>AB T5X 2K8</p>
    <ul class="contacts">
      <li><svg viewBox="0 0 24 24"><path d="M6.6 10.8a15 15 0 0 0 6.6 6.6l2.2-2.2a1 1 0 0 1 1-.25 11.4 11.4 0 0 0 3.6.57 1 1 0 0 1 1 1V20a1 1 0 0 1-1 1A17 17 0 0 1 3 4a1 1 0 0 1 1-1h3.5a1 1 0 0 1 1 1c0 1.25.2 2.45.57 3.57a1 1 0 0 1-.25 1z"/></svg>780.555.0148</li>
      <li><svg viewBox="0 0 24 24"><path d="M7 1h10a2 2 0 0 1 2 2v18a2 2 0 0 1-2 2H7a2 2 0 0 1-2-2V3a2 2 0 0 1 2-2zm0 3v15h10V4z"/></svg>780.555.0193</li>
      <li><svg viewBox="0 0 24 24"><path d="M2 5h20v14H2zm2 2v.5l8 5 8-5V7l-8 5z"/></svg>brent@korvanshieldgroup.example</li>
      <li><svg viewBox="0 0 24 24"><path d="M12 2a10 10 0 1 0 0 20 10 10 0 0 0 0-20zm0 2c1 1.3 1.8 3 2.2 5H9.8C10.2 7 11 5.3 12 4zM9.6 11h4.8a14 14 0 0 1 0 2H9.6a14 14 0 0 1 0-2zm.2 4h4.4c-.4 2-1.2 3.7-2.2 5-1-1.3-1.8-3-2.2-5z"/></svg>www.korvanshieldgroup.example</li>
    </ul>
  </section>

  <section class="card card-back" aria-label="Card back">
    <div class="emboss-brand">
      <p class="emboss-name">Korvan Shield Group</p>
      <div class="emboss-rule"></div>
    </div>
    <p class="services">Guards Mobiles Live Video Surveillance Access Intrusion</p>
  </section>
</main>
</body>
</html>
```